Flyer-Design für IT-Systemhaus
Zielgruppe
Wir sind ein IT Systemhaus mit einem Scherpunkt auf Wireless LAN für Gewerbekunden
https://www.kovalmar-beispiel.de/wlan-beratung/
Aufgabenstellung
Im Anhang finden Sie einige Stichpunkte/Texte und eine PPT mit Grafiken, sowie unser Briefpapier.
Ziel ist es 1 Flyer A4 Einseitig zu erhalten – Wir benötigen diesen As soon as possible
Das Thema lautet hier:
1. WLAN für Bauunternehmen / Elektriker
Grafiken können Sie aus der PPT oder der Webseite entnehmen
Die Flyer sollten im oberen Bereich wie unser Briefpapier aussehen und Farbmäßig unserem CD entsprechen
#1e73be
Den Orangeton finde ich leider gerade nicht ☹
An Ergänzenden Grafiken sind wir ebenfalls Interessiert.
Die Welle haben wir leider nicht als Vectorgrafik

```html
<!DOCTYPE html>
<html lang="de">
<head>
<meta charset="utf-8">
<title>Kovalmar – Flyer WLAN &amp; DigitalPakt</title>
<link href="https://fonts.googleapis.com/css2?family=Roboto:ital,wght@0,400;0,500;0,700;1,300;1,400;1,500;1,700&display=swap" rel="stylesheet">
<style>
  :root{
    --brand-blue:#1e73be;
    --wave-mid:#4aa3e0;
    --wave-light:#acd5f2;
    --accent-orange:#f07d1a;
    --text-dark:#4a4a4a;
    --text-body:#5a5a5a;
    --stage:#a5a5a5;
    --paper:#ffffff;
  }
  *{box-sizing:border-box;margin:0;padding:0}
  html,body{width:1200px;height:823px;overflow:hidden;background:var(--stage)}
  body{position:relative;font-family:"Roboto",Arial,sans-serif}
  .flyer{position:absolute;top:9px;width:566px;height:804px;background:var(--paper);overflow:hidden;box-shadow:0 1px 4px rgba(0,0,0,.25)}
  .flyer--wlan{left:13px}
  .flyer--school{left:621px}
  .flyer__art{position:absolute;inset:0;width:566px;height:804px}
  .brand{position:absolute;top:44px;right:42px;font-style:italic;font-weight:400;font-size:27px;letter-spacing:3px;color:var(--text-dark)}
  .flyer__title{position:absolute;left:24px;top:112px;font-style:italic;font-weight:500;font-size:28px;color:var(--brand-blue);letter-spacing:.2px;white-space:nowrap}
  .section{position:absolute;left:24px;width:300px}
  .section__head{font-style:italic;font-weight:500;font-size:13px;color:var(--text-dark);margin-bottom:8px}
  .bullets{list-style:none}
  .bullets li{position:relative;padding-left:16px;font-style:italic;font-weight:300;font-size:12px;line-height:17px;color:var(--text-body);margin-bottom:2px}
  .bullets li::before{content:"•";position:absolute;left:3px;top:0;font-size:9px;color:#888}
  .service{position:absolute;left:359px;display:flex;align-items:center;gap:16px}
  .service__icon{width:55px;height:55px;border:1px solid var(--brand-blue);border-radius:10px;display:flex;align-items:center;justify-content:center;background:#fff}
  .service__icon svg{width:38px;height:38px}
  .service__label{font-style:italic;font-weight:500;font-size:13px;line-height:16px;color:var(--brand-blue)}
  .benefits{position:absolute;left:16px;width:232px;background:var(--brand-blue);padding:16px 14px 10px 18px;color:#fff}
  .benefits__head{font-style:italic;font-weight:500;font-size:13.5px;margin-bottom:10px}
  .benefits__list{list-style:none}
  .benefits__list li{position:relative;padding-left:10px;font-style:italic;font-weight:400;font-size:10.5px;line-height:14px;margin-bottom:13px}
  .benefits__list li::before{content:"•";position:absolute;left:0;font-size:8px}
  .footer-contact{position:absolute;right:12px;bottom:10px;font-style:italic;font-weight:700;font-size:11.5px;color:#fff}
</style>
</head>
<body>

<!-- Flyer 1: WLAN für Bauunternehmen -->
<section class="flyer flyer--wlan">
  <svg class="flyer__art" viewBox="0 0 566 804" aria-hidden="true">
    <path d="M0 0H566V10C400 22 200 92 0 90Z" fill="var(--wave-light)"/>
    <path d="M0 0H566V4C380 12 200 62 0 64Z" fill="var(--wave-mid)"/>
    <path d="M0 0H460C300 10 150 36 0 44Z" fill="var(--brand-blue)"/>
  </svg>
  <div class="flyer__art" role="img" aria-label="Foto: Hände arbeiten an Bauplänen mit Lineal und Stift" style="clip-path:path('M150 804 L150 620 C260 560 420 490 566 455 L566 804 Z');background:linear-gradient(160deg,#f4efe8 0%,#e2d8cc 45%,#c8b8a6 80%,#b59f89 100%)"></div>
  <svg class="flyer__art" viewBox="0 0 566 804" aria-hidden="true">
    <path d="M0 804V792C200 742 400 728 566 716V804Z" fill="var(--wave-light)"/>
    <path d="M70 804C250 768 420 754 566 748V804Z" fill="var(--wave-mid)"/>
    <path d="M190 804C340 786 460 776 566 770V804Z" fill="var(--brand-blue)"/>
  </svg>

  <div class="brand">KOVALMAR</div>
  <h1 class="flyer__title">WLAN für Bauunternehmen &amp; Elektriker</h1>

  <div class="section" style="top:162px">
    <h2 class="section__head">Mehrwerte für Ihr Unternehmen:</h2>
    <ul class="bullets">
      <li>Alleinstellungsmarkmal gegenüber Mitbewerbern</li>
      <li>Schaffung neuer (monetärer) Mehrwerte</li>
      <li>Risikominderung für WLAN Fehlplanungen</li>
    </ul>
  </div>
  <div class="section" style="top:258px">
    <h2 class="section__head">Mehrwerte für Ihre Kunden:</h2>
    <ul class="bullets">
      <li>Professionelles WLAN bereits beim Einzug</li>
      <li>WLAN nach Stand der Technik</li>
      <li>Investitionskosten für WLAN bereits im Rahmen der Gebäudefinanzierung planbar</li>
      <li>Investitionskosten über Gebäudefinanzierung planbar</li>
    </ul>
  </div>
  <div class="section" style="top:408px;width:260px">
    <h2 class="section__head">Die Kovalmar GmbH bietet:</h2>
    <ul class="bullets">
      <li>Erfahrung mit Bauvorhaben in privaten und öffentlichen Bereichen</li>
      <li>ISO 9001 und ISO 27001 zertifiziert</li>
      <li>Professionelle WLAN-Beratung von Konzept bis zur Konfiguration</li>
    </ul>
  </div>

  <div class="service" style="top:221px">
    <div class="service__icon"><svg viewBox="0 0 40 40" fill="none" stroke="var(--accent-orange)" stroke-width="2.4"><rect x="6" y="7" width="26" height="24" rx="2"/><path d="M12 13h14v12H12z M19 13v6h7"/><path d="M26 32a6 6 0 0 1 8 0 M28.5 35a2.5 2.5 0 0 1 3 0" stroke-width="1.8"/></svg></div>
    <div class="service__label">WLAN Planung</div>
  </div>
  <div class="service" style="top:290px">
    <div class="service__icon"><svg viewBox="0 0 40 40" fill="none" stroke="var(--accent-orange)" stroke-width="2.4"><path d="M5 19L20 6l15 13 M9 16v18h22V16"/><circle cx="20" cy="22" r="2" fill="var(--accent-orange)"/><path d="M15 18a7 7 0 0 0 0 8 M25 18a7 7 0 0 1 0 8" stroke-width="1.8"/></svg></div>
    <div class="service__label">WLAN<br>Ausleuchtung</div>
  </div>
  <div class="service" style="top:360px">
    <div class="service__icon"><svg viewBox="0 0 40 40"><rect x="8" y="5" width="20" height="30" fill="var(--accent-orange)"/><g fill="#fff"><rect x="11" y="9" width="4" height="4"/><rect x="17" y="9" width="4" height="4"/><rect x="11" y="16" width="4" height="4"/><rect x="17" y="16" width="4" height="4"/><rect x="11" y="23" width="4" height="4"/></g><path d="M27 30a7 7 0 0 1 9 0 M29.5 33.5a3 3 0 0 1 4 0" stroke="var(--brand-blue)" stroke-width="1.8" fill="none"/></svg></div>
    <div class="service__label">WLAN<br>Infrastruktur</div>
  </div>

  <aside class="benefits" style="top:582px;height:204px">
    <h3 class="benefits__head">Ihre Vorteile auf einen Blick:</h3>
    <ul class="benefits__list">
      <li>Planung und Ausleuchtung vom Profi</li>
      <li>Konfiguration und Montage durch zertifizierte Techniker</li>
      <li>Kompetente und objektive Beratung vom Fachmann</li>
      <li>Maximale Effizienz und kalkulierbare Kosten</li>
    </ul>
  </aside>
  <div class="footer-contact">info@kovalmar-beispiel.de | www.kovalmar-beispiel.de</div>
</section>

<!-- Flyer 2: DigitalPakt Schulen -->
<section class="flyer flyer--school">
  <svg class="flyer__art" viewBox="0 0 566 804" aria-hidden="true">
    <path d="M0 0H566V10C400 22 200 92 0 90Z" fill="var(--wave-light)"/>
    <path d="M0 0H566V4C380 12 200 62 0 64Z" fill="var(--wave-mid)"/>
    <path d="M0 0H460C300 10 150 36 0 44Z" fill="var(--brand-blue)"/>
  </svg>
  <div class="flyer__art" role="img" aria-label="Foto: Schüler arbeitet im Klassenzimmer an einem Tablet" style="clip-path:path('M240 804 L240 560 C350 530 460 490 566 470 L566 804 Z');background:linear-gradient(150deg,#efe4d6 0%,#dcc6ac 40%,#8aa3c4 70%,#2f4f86 100%)"></div>
  <svg class="flyer__art" viewBox="0 0 566 804" aria-hidden="true">
    <path d="M0 804V792C200 742 400 728 566 716V804Z" fill="var(--wave-light)"/>
    <path d="M70 804C250 768 420 754 566 748V804Z" fill="var(--wave-mid)"/>
    <path d="M190 804C340 786 460 776 566 770V804Z" fill="var(--brand-blue)"/>
  </svg>

  <div class="brand">KOVALMAR</div>
  <h1 class="flyer__title" style="top:104px">DigitalPakt Schulen</h1>

  <div class="section" style="top:162px">
    <h2 class="section__head">Mehrwert für die Schule:</h2>
    <ul class="bullets">
      <li>90% der Kosten werden vom Staat übernommen</li>
      <li>Reputationsvorteil durch digitales Lernangebot</li>
      <li>Moderne Unterrichtsmethoden</li>
    </ul>
  </div>
  <div class="section" style="top:272px">
    <h2 class="section__head">Mehrwert für die Schüler:</h2>
    <ul class="bullets">
      <li>Routinierter Umgang mit modernen Medien</li>
      <li>Verbesserte Lernerfolge</li>
      <li>Zeitgemäße Medienkompetenzen</li>
    </ul>
  </div>
  <div class="section" style="top:380px">
    <h2 class="section__head">Die Kovalmar GmbH bietet:</h2>
    <ul class="bullets">
      <li>Unterstützung während der Antragsstellung</li>
      <li>Erfahrung mit Schulen</li>
      <li>Professionelle WLAN-Beratung von Konzept bis zur Konfiguration</li>
    </ul>
  </div>

  <div class="service" style="top:207px">
    <div class="service__icon"><svg viewBox="0 0 40 40" fill="none" stroke="var(--accent-orange)" stroke-width="3.2" stroke-linecap="round"><path d="M5 16a21 21 0 0 1 30 0 M10 22a14 14 0 0 1 20 0 M15 28a7 7 0 0 1 10 0"/><circle cx="20" cy="33" r="1.8" fill="var(--accent-orange)"/></svg></div>
    <div class="service__label">WLAN Lösungen</div>
  </div>
  <div class="service" style="top:277px">
    <div class="service__icon"><svg viewBox="0 0 40 40"><rect x="4" y="6" width="32" height="22" rx="2" fill="var(--accent-orange)"/><rect x="7" y="9" width="26" height="16" fill="#fff"/><rect x="15" y="28" width="8" height="5" fill="var(--accent-orange)"/><rect x="11" y="33" width="14" height="2" fill="var(--accent-orange)"/><rect x="27" y="28" width="10" height="8" rx="1" fill="var(--brand-blue)"/><path d="M29.5 28v-2a2.5 2.5 0 0 1 5 0v2" stroke="var(--brand-blue)" stroke-width="1.6" fill="none"/></svg></div>
    <div class="service__label">IT Sicherheit</div>
  </div>
  <div class="service" style="top:348px">
    <div class="service__icon"><svg viewBox="0 0 40 40" fill="none" stroke="var(--accent-orange)" stroke-width="2.6"><path d="M8 22v-3a12 12 0 0 1 24 0v3"/><rect x="5" y="20" width="6" height="9" rx="2" fill="var(--accent-orange)"/><rect x="29" y="20" width="6" height="9" rx="2" fill="var(--accent-orange)"/><path d="M32 29c0 4-4 6-9 6"/><circle cx="30" cy="34" r="4" fill="var(--brand-blue)" stroke="none"/></svg></div>
    <div class="service__label">Support vom<br>Fachmann</div>
  </div>

  <aside class="benefits" style="top:502px;height:284px">
    <h3 class="benefits__head">Ihre Vorteile auf einen Blick:</h3>
    <ul class="benefits__list">
      <li>Integration von modernen Lernmethoden</li>
      <li>Ständig verfügbare, digitale Lernumgebungen</li>
      <li>Digitale Kommunikationswege zwischen Lehrern und Schülern</li>
      <li>Direktes Feedback für Schüler und Lehrer</li>
      <li>Einbindung von BYOD-Konzepten und Screencasting</li>
      <li>Remote-Zugriff auf den Unterricht von Zuhause</li>
    </ul>
  </aside>
  <div class="footer-contact">info@kovalmar-beispiel.de | www.kovalmar-beispiel.de</div>
</section>

</body>
</html>
```